Business Card Design Project

www.tallorivault.com is our website. We are a technology company that provides brokers, lawyers and accountants with an cloud based paperless facilitation and revenue stream that facilitates their clients Health spending accounts.

Target Market(s)

Insurance brokers, lawyers and accountants

Industry/Entity Type

Business

```html
<!DOCTYPE html>
<html lang="en">
<head>
<meta charset="utf-8">
<title>Tallori Business Card</title>
<link rel="stylesheet" href="https://fonts.googleapis.com/css2?family=Arimo:ital,wght@0,400;0,700;1,700&family=Tinos:ital,wght@1,700&display=swap">
<style>
  :root {
    --brand-blue: #00aeef;
    --brand-blue-deep: #1b8fd0;
    --ink: #3a3a3a;
    --ink-blue: #0a5a9c;
    --pale: #e8f6fd;
    --sky: #bfe6f8;
    --white: #ffffff;
    --social: #2f6fb3;
  }
  * { margin: 0; padding: 0; box-sizing: border-box; }
  html, body { width: 1200px; height: 395px; overflow: hidden; background: var(--white); }
  body { position: relative; font-family: "Arimo", Arial, sans-serif; color: var(--ink); }

  .card {
    position: absolute; top: 53px; width: 508px; height: 290px; overflow: hidden;
    box-shadow: 4px 5px 7px rgba(0,0,0,0.35);
  }
  .card--front { left: 62px; background: linear-gradient(100deg, var(--white) 0%, var(--pale) 40%, var(--sky) 100%); }
  .card--back { left: 621px; background: var(--brand-blue); }

  .front__photo {
    position: absolute; left: 281px; top: 0; width: 227px; height: 99px;
    background: linear-gradient(90deg, rgba(200,225,240,0) 0%, #c9dde9 35%, #b7cfdf 70%, #a9c4d6 100%);
  }
  .front__lower {
    position: absolute; left: 0; top: 99px; width: 508px; height: 162px;
    background: linear-gradient(100deg, rgba(255,255,255,0) 30%, rgba(120,205,240,0.45) 100%);
  }

  .brand { position: absolute; display: flex; align-items: center; gap: 6px; color: var(--brand-blue-deep); font-weight: 700; }
  .brand__dot { border-radius: 50%; background: var(--brand-blue); }
  .front__brand { left: 44px; top: 56px; font-size: 30px; }
  .front__brand .brand__dot { width: 16px; height: 16px; }

  .person { position: absolute; left: 118px; top: 107px; display: flex; align-items: center; }
  .person__name { font-family: "Tinos", Georgia, serif; font-style: italic; font-weight: 700; font-size: 16px; color: var(--ink); letter-spacing: 0.5px; }
  .person__rule { width: 2px; height: 24px; background: var(--brand-blue); margin: 0 6px 0 8px; }
  .person__title { font-size: 11px; color: var(--ink); }

  .contacts { position: absolute; list-style: none; font-size: 13px; line-height: 17px; }
  .contacts li { display: flex; align-items: flex-start; }
  .contacts svg { width: 11px; height: 11px; margin: 3px 9px 0 0; flex: none; }
  .contacts--phones { left: 58px; top: 145px; }
  .contacts--details { left: 236px; top: 143px; }
  .contacts--details .indent { padding-left: 20px; }

  .divider { position: absolute; left: 203px; top: 146px; width: 2px; height: 60px; background: linear-gradient(var(--white), var(--brand-blue), var(--white)); }

  .social { position: absolute; top: 219px; display: flex; align-items: center; justify-content: center; width: 37px; height: 37px; border-radius: 4px; background: var(--social); color: var(--white); font-size: 9px; font-weight: 700; }
  .social--flock { left: 356px; }
  .social--chirp { left: 411px; background: var(--brand-blue); }
  .social--nexo { left: 460px; background: var(--brand-blue-deep); }

  .band { position: absolute; left: 0; top: 261px; width: 508px; height: 29px; background: var(--brand-blue); }
  .band__tagline { color: var(--white); font-weight: 700; font-style: italic; font-size: 13.5px; line-height: 29px; padding-left: 77px; }

  .back__cloud {
    position: absolute; left: 0; top: 20px; width: 508px; height: 241px;
    background: radial-gradient(ellipse 55% 60% at 50% 60%, var(--white) 0%, #d6effb 55%, rgba(191,230,248,0.9) 75%, rgba(0,174,239,0) 100%);
  }
  .back__brand { left: 0; right: 0; top: 128px; justify-content: center; font-size: 58px; }
  .back__brand .brand__dot { width: 26px; height: 26px; }
  .back__tagline { position: absolute; left: 0; right: 0; top: 228px; text-align: center; font-size: 10.5px; color: var(--ink-blue); }
</style>
</head>
<body>
  <section class="card card--front">
    <div class="front__photo" role="img" aria-label="Photo of a healthcare worker in a surgical mask"></div>
    <div class="front__lower"></div>

    <div class="brand front__brand"><span class="brand__dot"></span>Tallori</div>

    <div class="person">
      <span class="person__name">Tallori Salesman</span>
      <span class="person__rule"></span>
      <span class="person__title">Director of Sles</span>
    </div>

    <ul class="contacts contacts--phones">
      <li><svg viewBox="0 0 12 12"><circle cx="6" cy="6" r="5.2" fill="none" stroke="#1b8fd0" stroke-width="1.4"/><path d="M4 3.5c0 2.5 1.5 4.5 4 5l.6-1.2-1.4-.7-.6.6c-.9-.5-1.5-1.2-1.8-2l.6-.6-.6-1.4z" fill="#1b8fd0"/></svg>555 014 2280</li>
      <li><svg viewBox="0 0 12 12"><rect x="3" y="1" width="6" height="3" fill="#1b8fd0"/><rect x="1" y="4" width="10" height="5" rx="1" fill="#1b8fd0"/><rect x="3" y="7" width="6" height="4" fill="#fff" stroke="#1b8fd0"/></svg>555 014 2281</li>
      <li><svg viewBox="0 0 12 12"><rect x="3" y="1" width="6" height="10" rx="1.2" fill="#1b8fd0"/><rect x="4" y="2.5" width="4" height="4" fill="#fff"/></svg>555 014 2282</li>
    </ul>

    <div class="divider"></div>

    <ul class="contacts contacts--details">
      <li><svg viewBox="0 0 12 12"><rect x="1" y="2.5" width="10" height="7" fill="none" stroke="#1b8fd0" stroke-width="1.3"/><path d="M1 2.5l5 4 5-4" fill="none" stroke="#1b8fd0" stroke-width="1.3"/></svg>sales@tallorivault.com</li>
      <li><svg viewBox="0 0 12 12"><circle cx="6" cy="6" r="5" fill="none" stroke="#1b8fd0" stroke-width="1.2"/><ellipse cx="6" cy="6" rx="2.2" ry="5" fill="none" stroke="#1b8fd0"/><path d="M1 6h10" stroke="#1b8fd0"/></svg>www.tallorivault.com</li>
      <li><svg viewBox="0 0 12 12"><path d="M6 1L1 6h1.5v5h3V8h1v3h3V6H11z" fill="#1b8fd0"/></svg>Suite 410, 2290 - 5th Avenue SE</li>
      <li class="indent">Calgary, AB&nbsp; T2G 4K1</li>
    </ul>

    <span class="social social--flock">Flock</span>
    <span class="social social--chirp">Chirp</span>
    <span class="social social--nexo">Nexo</span>

    <div class="band"><p class="band__tagline">Your clients Health Spending Account, Made Simple</p></div>
  </section>

  <section class="card card--back">
    <div class="back__cloud" role="img" aria-label="Large soft white cloud shape behind the brand name"></div>
    <div class="brand back__brand"><span class="brand__dot"></span>Tallori</div>
    <p class="back__tagline">Your Clients&nbsp;&nbsp;Health Spending Account, Made Simple</p>
  </section>
</body>
</html>
```